Tomas's Business Cards

My husband is a self employed Cabinet Maker... who contracts to Building companies and clients directly.
He installs kitchesn, designs and also completes renovations and building work.

I would like a small, FUNKY, simple but eye catching design.

It needs to incorporate the following.
Custom Cabinets / Installations / Renovations / Design

Commercial and Residential

He does not have a Website or Chatterly,
contact number is 0438 207 619 and email is tomasvelkin@quillmail.example

I would like a Grey/Silver on black, or blue covering.. I am open to colour designs?

Thank you. :-)

Target Market(s)

Building Companies
Clients
Other Trades people onsite,. to give out at job sites

Industry/Entity Type

Business

Contact Information for Business Card

Phone: 0438 207 619
Email: tomasvelkin@quillmail.example

Font styles to use
Sans Serif

Colors
0592cd
747474
474747
1b1b1b
85cae6

Requirements
Must have
• Funky, simple, eye catching design
• Would like use of Silver/Grey - and a colour that would complement this.
• Am open to ideas :-)
Nice to have
• We do not have a logo or picture, will leave this up to you if you think an image would be beneficial???
• Thank you.

```html
<!DOCTYPE html>
<html lang="en">
<head>
<meta charset="utf-8">
<title>Tomas Velkin – Business Card</title>
<link rel="stylesheet" href="https://fonts.googleapis.com/css2?family=Patrick+Hand+SC&family=Quicksand:wght@500;600;700&display=swap">
<style>
  :root {
    --stage: #d9d9d9;
    --card-light: #f4f2ee;
    --card-mid: #e6e2da;
    --blue: #0592cd;
    --blue-soft: #85cae6;
    --ink: #1b1b1b;
    --ink-mid: #474747;
    --grey: #747474;
  }
  html, body {
    margin: 0;
    width: 1200px;
    height: 873px;
    overflow: hidden;
    background: var(--stage);
  }
  .stage {
    width: 1200px;
    height: 873px;
    display: flex;
    align-items: center;
    justify-content: center;
  }
  .card {
    position: relative;
    width: 840px;
    height: 480px;
    box-shadow: 0 10px 30px rgba(0,0,0,.18);
    overflow: hidden;
  }
  .card__texture {
    position: absolute;
    inset: 0;
    background: linear-gradient(180deg, var(--card-light) 0%, var(--card-mid) 50%, var(--card-light) 100%);
  }
  .card__content {
    position: absolute;
    top: 44px;
    right: 56px;
    width: 640px;
    display: flex;
    flex-direction: column;
    align-items: flex-end;
    font-family: "Quicksand", sans-serif;
    color: var(--ink);
  }
  .services {
    font-size: 15px;
    font-weight: 600;
    letter-spacing: .04em;
    color: var(--ink-mid);
    text-transform: uppercase;
  }
  .rule {
    width: 410px;
    height: 2px;
    background: var(--blue);
    margin: 12px 0 10px;
  }
  .sector {
    font-size: 24px;
    font-weight: 600;
    color: var(--ink);
  }
  .name {
    align-self: flex-start;
    margin: 30px 0 0 60px;
    font-family: "Patrick Hand SC", sans-serif;
    font-size: 76px;
    line-height: 1;
    color: var(--blue);
    text-shadow: 1px 1px 0 var(--blue-soft);
  }
  .contact {
    align-self: flex-start;
    margin: 34px 0 0 0;
    display: flex;
    flex-direction: column;
    gap: 8px;
  }
  .contact__line {
    font-size: 30px;
    font-weight: 700;
    color: var(--ink);
    white-space: nowrap;
  }
  .contact__line--phone { padding-left: 110px; }
  .contact__label {
    font-size: 17px;
    font-weight: 600;
    color: var(--blue);
    margin-right: 6px;
  }
</style>
</head>
<body>
  <main class="stage">
    <article class="card">
      <div class="card__texture" role="img" aria-label="Light whitewashed wood grain texture"></div>
      <div class="card__content">
        <p class="services" style="margin:0">Custom Cabinets | Installations | Renovations | Design</p>
        <div class="rule"></div>
        <p class="sector" style="margin:0">Commercial and Residential</p>
        <h1 class="name" style="font-weight:400">Tomas Velkin</h1>
        <div class="contact">
          <p class="contact__line contact__line--phone" style="margin:0"><span class="contact__label">phone:</span>0438 207 619</p>
          <p class="contact__line" style="margin:0"><span class="contact__label">email:</span>TOMASVELKIN@QUILLMAIL.EXAMPLE</p>
        </div>
      </div>
    </article>
  </main>
</body>
</html>
```